We are an integrated facilities management company.

We aggregate everything related to facilities maintenance. Repair-replacement of equipment and facility space materials from:
Asset gathering and tracking.
Vendor screening, contracting and management.
Service requirement development.
Work order processing and management.
Invoice reconciliation.
Vendor payment.
Reporting.
Capital equipment bids and project management.

Target Market(s)

Retail, hospitality, multi-family housing, long term healthcare.

Industry/Entity Type

Maintenance

Contact Information for Business Card

Professional and bold look. (see logo zip file)

Colors
3377b5
85abd2
cedeed

Requirements
Must have
• N/A
Nice to have
• N/A
Should not have
• N/A

```html
<!DOCTYPE html>
<html lang="en">
<head>
<meta charset="utf-8">
<title>Steadfast Facility Partners — Business Card</title>
<link rel="stylesheet" href="https://fonts.googleapis.com/css2?family=Open+Sans:wght@400;600&family=Montserrat:wght@300;600&display=swap">
<style>
  :root {
    --canvas: #e4e5e7;
    --card: #2d2d2f;
    --card-back-light: #5a5a5c;
    --card-back-dark: #161617;
    --blue: #3377b5;
    --blue-mid: #85abd2;
    --blue-pale: #cedeed;
    --text: #f2f2f2;
    --muted: #8d8d90;
    --rule: #6b6b6e;
  }
  * { box-sizing: border-box; margin: 0; padding: 0; }
  html, body { width: 1200px; height: 1021px; overflow: hidden; }
  body {
    background: var(--canvas);
    font-family: "Open Sans", sans-serif;
    display: flex; flex-direction: column; align-items: center; justify-content: center;
    gap: 56px;
  }
  .card {
    width: 700px; height: 400px;
    position: relative; overflow: hidden;
    box-shadow: 0 10px 30px rgba(0,0,0,.25);
  }
  /* back */
  .card-back { background: var(--card-back-dark); }
  .card-back .pattern-area {
    position: absolute; inset: 0;
    background: linear-gradient(120deg, var(--card-back-light) 0%, #333335 45%, var(--card-back-dark) 100%);
  }
  .card-back .tagline-row {
    position: absolute; left: 150px; top: 182px;
    display: flex; align-items: center; gap: 22px;
  }
  .card-back .mark-square { width: 30px; height: 30px; background: var(--blue); }
  .card-back .tagline {
    font-family: "Montserrat", sans-serif; font-weight: 300;
    font-size: 15px; letter-spacing: 7px; color: var(--muted);
  }
  /* front */
  .card-front { background: var(--card); }
  .brand {
    position: absolute; left: 60px; top: 168px; width: 260px;
    display: flex; align-items: center; gap: 12px;
  }
  .brand .mark-square { width: 44px; height: 44px; background: var(--blue); flex: none; }
  .brand .brand-name {
    font-weight: 600; font-size: 20px; line-height: 1.15; color: var(--blue-mid);
    text-transform: uppercase; letter-spacing: .5px;
  }
  .brand-tagline {
    position: absolute; left: 116px; top: 222px;
    font-family: "Montserrat", sans-serif; font-weight: 300;
    font-size: 9px; letter-spacing: 2.5px; color: var(--muted);
  }
  .divider {
    position: absolute; left: 350px; top: 88px; width: 1px; height: 230px;
    background: var(--rule);
  }
  .contact { position: absolute; left: 385px; top: 95px; color: var(--text); }
  .contact .name { color: var(--blue); font-weight: 600; font-size: 21px; }
  .contact .role { font-size: 15px; margin-bottom: 18px; }
  .contact .address { font-size: 15px; line-height: 1.35; }
  .contact ul { list-style: none; margin-top: 4px; }
  .contact li { display: flex; align-items: center; gap: 12px; font-size: 15px; line-height: 1.45; }
  .contact li svg { width: 14px; height: 14px; flex: none; }
</style>
</head>
<body>
  <section class="card card-back">
    <div class="pattern-area" role="img" aria-label="Repeating brand monogram pattern fading from grey to black"></div>
    <div class="tagline-row">
      <span class="mark-square"></span>
      <span class="tagline">MAINTAIN • REPAIR • REPLACE</span>
    </div>
  </section>

  <section class="card card-front">
    <div class="brand">
      <span class="mark-square"></span>
      <span class="brand-name">Steadfast Facility Partners</span>
    </div>
    <div class="brand-tagline">MAINTAIN • REPAIR • REPLACE</div>
    <div class="divider"></div>
    <div class="contact">
      <div class="name">Daniel Reyes</div>
      <div class="role">Founder</div>
      <div class="address">450 Harbor Street, Suite 310<br>Tampa, Florida, 33602</div>
      <ul>
        <li>
          <svg viewBox="0 0 24 24"><path fill="#3377b5" d="M6.6 10.8a15 15 0 0 0 6.6 6.6l2.2-2.2c.3-.3.7-.4 1-.2 1.1.4 2.3.6 3.6.6.6 0 1 .4 1 1V20c0 .6-.4 1-1 1A17 17 0 0 1 3 4c0-.6.4-1 1-1h3.5c.6 0 1 .4 1 1 0 1.3.2 2.5.6 3.6.1.3 0 .7-.2 1z"/></svg>
          (555) 014-2290
        </li>
        <li>
          <svg viewBox="0 0 24 24" fill="none" stroke="#3377b5" stroke-width="2"><rect x="2" y="5" width="20" height="14"/><path d="M2 5l10 8 10-8"/></svg>
          daniel@steadfastfacility.com
        </li>
        <li>
          <svg viewBox="0 0 24 24" fill="none" stroke="#3377b5" stroke-width="2"><circle cx="12" cy="12" r="10"/><path d="M2 12h20M12 2c3 3 3 17 0 20M12 2c-3 3-3 17 0 20"/></svg>
          www.steadfastfacility.com
        </li>
      </ul>
    </div>
  </section>
</body>
</html>
```